Business cards and logo for kitchen and bath remodeling company

We want an elegant card but that calls attention something unique and when people see it they remember us. A log that we can use for our own. We are a kitchen and bathroom remodeling company. We are 3 partners staring the company we are located in seattle washington usa. We try to give the best experience and luxury look in our projects and we are looking to show that in our cards. I added a sample of a card I really like. I like the black and gold look but gray blue or green in a metallic look would look nice. I'm open to any color.

Target Market(s)

Home owners.

Industry/Entity Type

Construction

Contact Information for Business Card

Larchmont and Vey builders

Colors

Designer to choose colors to be used in the design.

Requirements
Must have
• Make a Logo
• Logo to be unique
• Name of company larchmont and vey builders
Nice to have
• Have a good color scheme
• Front design to connect with back of card

```html
<!DOCTYPE html>
<html lang="en">
<head>
<meta charset="utf-8">
<title>Larchmont and Vey Builders — Business Cards</title>
<link rel="stylesheet" href="https://fonts.googleapis.com/css2?family=Quicksand:wght@300;400;500&display=swap">
<style>
  :root {
    --stage: #8e8e90;
    --card: #2a2a28;
    --accent: #f28c1c;
  }
  * { box-sizing: border-box; margin: 0; padding: 0; }
  html, body { width: 1200px; height: 835px; overflow: hidden; }
  body {
    background: var(--stage);
    font-family: "Quicksand", sans-serif;
    display: flex;
    align-items: center;
    justify-content: center;
    gap: 40px;
  }
  .card {
    position: relative;
    width: 540px;
    height: 309px;
    background: var(--card);
    overflow: hidden;
    color: var(--accent);
  }
  .card__tab {
    position: absolute;
    top: 0;
    left: 50%;
    width: 56px;
    height: 28px;
    margin-left: -28px;
    background: var(--accent);
    border-radius: 0 0 28px 28px;
  }

  /* Front */
  .front__band {
    position: absolute;
    left: 0; right: 0; bottom: 0;
    height: 14px;
    background: var(--accent);
  }
  .front__square {
    position: absolute;
    top: 88px;
    left: 50%;
    width: 62px;
    height: 62px;
    margin-left: -31px;
    border: 1.5px solid var(--accent);
  }
  .front__name {
    position: absolute;
    top: 182px;
    left: 0; right: 0;
    text-align: center;
    font-weight: 500;
    font-size: 19px;
    letter-spacing: 3px;
  }

  /* Back */
  .back__name {
    position: absolute;
    top: 62px;
    right: 44px;
    font-weight: 300;
    font-size: 30px;
    letter-spacing: 5px;
    white-space: nowrap;
  }
  .back__rule-top {
    position: absolute;
    top: 106px;
    right: 250px;
    width: 84px;
    height: 1.5px;
    background: var(--accent);
  }
  .back__phone {
    position: absolute;
    top: 110px;
    right: 60px;
    font-weight: 400;
    font-size: 14px;
    letter-spacing: 2px;
    white-space: nowrap;
  }
  .back__rule-bottom {
    position: absolute;
    top: 136px;
    right: 44px;
    width: 150px;
    height: 1.5px;
    background: var(--accent);
  }
  .back__contact {
    position: absolute;
    left: 40px;
    bottom: 72px;
    font-weight: 400;
    font-size: 13px;
    line-height: 1.45;
    letter-spacing: 1px;
  }
  .back__stripe {
    position: absolute;
    left: 0; right: 0;
    bottom: 34px;
    height: 7px;
    background: var(--accent);
  }
</style>
</head>
<body>

  <section class="card card--front" aria-label="Card front">
    <div class="card__tab"></div>
    <div class="front__square"></div>
    <div class="front__name">Larchmont and Vey Builders</div>
    <div class="front__band"></div>
  </section>

  <section class="card card--back" aria-label="Card back">
    <div class="card__tab"></div>
    <div class="back__name">Dorian Achterberg</div>
    <div class="back__rule-top"></div>
    <div class="back__phone">Phone: 2065550147</div>
    <div class="back__rule-bottom"></div>
    <div class="back__contact">
      <div>dorian@larchmontvey.com</div>
      <div>larchmontvey.com</div>
    </div>
    <div class="back__stripe"></div>
  </section>

</body>
</html>
```